Innovative Freezer Label Design

Create a versatile and innovative freezer label design with universal appeal, suitable for different functionalities. The design should cater to a diverse audience, including those who freeze meals for meal prepping, batch cooking, and the restaurant industry. Our vision is a visually striking and distinctive design that embodies simplicity.

Example "our current labels feature essential details like "Contents" and "Date." We recognize these as crucial points of information. Currently, the challenge lies in creating various labels for different marketplaces, considering language barriers. A proposed solution involves the integration of universal icons to replace specific words, promoting practicality for international sales."

Kindly note that design concepts should not be restricted to our current product, brand guideline, logo, or the provided example.

Our goal is not only product differentiation but also increased sales through a blend of functionality and aesthetics.

The following are examples of freezer labels designs. Kindly do not restrict your designs to the examples. The designs must be universal (for language barrier purposes)

Examples:
https://www.snaprovel.co.uk/pin/5820174630298837415/
https://www.snaprovel.co.uk/pin/5820174630298837419/
https://www.snaprovel.co.uk/pin/5820174630298837408/
https://www.snaprovel.co.uk/pin/5820174630298837322/
https://www.snaprovel.co.uk/pin/5820174630298898764/

Please reach out if you have any questions.

Thank you

```html
<!DOCTYPE html>
<html lang="en">
<head>
<meta charset="UTF-8">
<title>Freezer Label – Contents &amp; Date</title>
<link href="https://fonts.googleapis.com/css2?family=Montserrat:wght@600&display=swap" rel="stylesheet">
<style>
  :root {
    --backdrop: #eceae4;
    --label-white: #ffffff;
    --field-cream: #f8f6ee;
    --ink: #2f3030;
    --rule: #8a8a86;
    --tone-orange: #ec6a3c;
    --tone-yellow: #f2b83a;
    --tone-sage: #7d8a6a;
    --tone-charcoal: #2e3431;
  }
  html, body {
    margin: 0;
    width: 1200px;
    height: 1200px;
    overflow: hidden;
    background: var(--backdrop);
    font-family: "Montserrat", sans-serif;
  }
  .canvas {
    position: relative;
    width: 1200px;
    height: 1200px;
  }
  .freezer-label {
    position: absolute;
    left: 140px;
    top: 140px;
    width: 920px;
    height: 920px;
    border-radius: 50%;
    background: var(--label-white);
    box-shadow: 0 6px 24px rgba(0,0,0,0.12);
  }
  .fruit-border {
    position: absolute;
    inset: 0;
  }
  .write-field {
    position: absolute;
    left: 140px;
    top: 140px;
    width: 640px;
    height: 640px;
    border-radius: 50%;
    background: var(--field-cream);
  }
  .field-icon {
    position: absolute;
    left: 420px;
    width: 80px;
    height: 80px;
  }
  .field-icon--contents { top: 279px; }
  .field-icon--date { top: 452px; }
  .field-icon * {
    fill: none;
    stroke: var(--ink);
    stroke-width: 5;
    stroke-linecap: round;
    stroke-linejoin: round;
  }
  .write-line {
    position: absolute;
    left: 245px;
    width: 430px;
    height: 3px;
    background: var(--rule);
  }
  .write-line--contents { top: 420px; }
  .write-line--date { top: 589px; }
</style>
</head>
<body>
<div class="canvas">
  <div class="freezer-label">
    <svg class="fruit-border" width="920" height="920" viewBox="0 0 920 920" role="img" aria-label="Wreath of flat fruit and leaf illustrations around the label: citrus slices, berries, pears and leaves in orange, yellow, sage and charcoal">
      <defs>
        <linearGradient id="wreathTones" x1="0" y1="0" x2="1" y2="1">
          <stop offset="0" stop-color="var(--tone-orange)"/>
          <stop offset="0.35" stop-color="var(--tone-yellow)"/>
          <stop offset="0.65" stop-color="var(--tone-sage)"/>
          <stop offset="1" stop-color="var(--tone-charcoal)"/>
        </linearGradient>
      </defs>
      <circle cx="460" cy="460" r="390" fill="none" stroke="url(#wreathTones)" stroke-width="110" opacity="0.55"/>
    </svg>
    <div class="write-field"></div>

    <svg class="field-icon field-icon--contents" viewBox="0 0 80 80" role="img" aria-label="Contents">
      <rect x="24" y="8" width="32" height="10" rx="3"/>
      <path d="M22 18 H58 Q66 24 66 34 V66 Q66 74 58 74 H22 Q14 74 14 66 V34 Q14 24 22 18 Z"/>
      <line x1="24" y1="46" x2="56" y2="46"/>
      <line x1="24" y1="58" x2="48" y2="58"/>
    </svg>
    <div class="write-line write-line--contents"></div>

    <svg class="field-icon field-icon--date" viewBox="0 0 80 80" role="img" aria-label="Date">
      <rect x="10" y="16" width="60" height="56" rx="6"/>
      <line x1="10" y1="32" x2="70" y2="32"/>
      <line x1="26" y1="8" x2="26" y2="22"/>
      <line x1="54" y1="8" x2="54" y2="22"/>
      <line x1="22" y1="46" x2="30" y2="46"/>
      <line x1="36" y1="46" x2="44" y2="46"/>
      <line x1="50" y1="46" x2="58" y2="46"/>
      <line x1="22" y1="59" x2="30" y2="59"/>
      <line x1="36" y1="59" x2="44" y2="59"/>
    </svg>
    <div class="write-line write-line--date"></div>
  </div>
</div>
</body>
</html>
```